MeadowLantern.com

Updated Website Structure for MeadowLantern.com
1. Home Page

(Add social media links in footer or sidebar)
Suggested addition:

Stay Connected
Follow Meadow Lantern for daily encouragement, calming tools, and community stories.

[Facebook Icon] [Instagram Icon] [YouTube Icon]
@MeadowLanternHome

2. How It Works

(No major change — keep focused on process and trust building)

3. Ebook Store

(Add social links at the bottom of the page)

Want more free content?
Follow us on social media for sneak peeks, affirmations, and updates on new releases!

[Facebook] [Instagram] [YouTube]

4. Certification Page

(Optional social proof addition)

Connect with Certified Meadow Lanterns
Join our online community and see real stories of growth and courage.

Follow us on social media to see how others are supporting each other:

5. Membership Tiers

(Keep page simple, but can include icons in footer)

6. About Me

Suggested addition:

Let’s Stay Connected
I love hearing from others walking this path.

Facebook: @MeadowLanternHome

Instagram: @MeadowLanternHome

YouTube: Meadow Lantern Channel

7. Disclosure Page

(Keep links in footer only for professional feel.)

8. Global Footer (Site-wide)

Every page should include a calming footer with:

Navigation links (Home | About Me | How It Works | Ebook Store | Certification | Membership | Disclosure)

Social media icons

Copyright info

Example footer text:

🌿 Walking with fear, choosing courage, calming the nervous system together.

© 2025 MeadowLantern.com | All rights reserved

```html
<!DOCTYPE html>
<html lang="en">
<head>
<meta charset="utf-8">
<title>Meadow Lanterns — Home</title>
<link href="https://fonts.googleapis.com/css2?family=Inter:wght@400;500;600&family=Manrope:wght@700;800&display=swap" rel="stylesheet">
<style>
  :root{
    --bg:#fff4fa;
    --white:#ffffff;
    --ink:#22102e;
    --body:#3b2d43;
    --muted:#4a3d52;
    --link:#5b18d6;
    --pink:#d95bbf;
    --pink-2:#c763d6;
    --line:#f0dbe9;
    --card-title:#6a3f62;
    --brand-dot:#efc3e6;
  }
  *{box-sizing:border-box;margin:0;padding:0}
  html,body{width:1200px;height:890px;overflow:hidden}
  body{background:var(--bg);font-family:"Inter",sans-serif;color:var(--body);position:relative}
  a{color:var(--link);text-decoration:none}

  .site-header{position:absolute;left:0;top:0;width:1200px;height:50px;border-bottom:1px solid var(--line);background:var(--bg)}
  .brand{position:absolute;left:200px;top:8px;display:flex;align-items:center;gap:8px}
  .brand-dot{width:34px;height:34px;border-radius:50%;background:var(--brand-dot)}
  .brand-name{font-weight:600;font-size:13px;color:var(--link)}
  .main-nav{position:absolute;left:405px;top:14px;height:22px;display:flex;align-items:center;gap:24px;font-size:10px}
  .main-nav a.current{font-weight:600}
  .btn-shop{background:linear-gradient(90deg,var(--pink),var(--pink-2));color:var(--white)!important;padding:5px 7px;border-radius:6px;margin-left:-6px;box-shadow:0 3px 8px rgba(217,91,191,.3)}

  .hero-card{position:absolute;left:194px;top:153px;width:437px;height:233px;background:linear-gradient(135deg,#fde4f3,#fff0f8);border-radius:12px;padding:15px;box-shadow:0 8px 20px rgba(217,91,191,.08)}
  .eyebrow{display:inline-block;background:var(--white);border:1px solid var(--line);border-radius:20px;font-size:8.5px;font-weight:600;color:var(--ink);padding:3px 6px}
  .hero-title{font-family:"Manrope",sans-serif;font-weight:800;font-size:29px;line-height:35px;color:var(--ink);margin-top:4px;letter-spacing:-.3px}
  .hero-lead{font-size:9.6px;line-height:16px;margin-top:7px;color:var(--muted)}
  .hero-actions{display:flex;gap:10px;margin-top:10px}
  .btn{font-size:10px;padding:6px 9px;border-radius:8px;border:1px solid var(--line);background:var(--white)}
  .btn-primary{background:linear-gradient(90deg,var(--pink),var(--pink-2));color:var(--white);border-color:transparent;box-shadow:0 4px 10px rgba(217,91,191,.35)}

  .portrait-card{position:absolute;left:650px;top:71px;width:356px;height:398px;background:var(--white);border:1px solid var(--line);border-radius:10px;padding:10px}
  .portrait{width:335px;height:335px;border-radius:8px;background:linear-gradient(160deg,#e9e4e0 0%,#d9c9c0 45%,#c0302e 75%,#a61f24 100%)}
  .portrait-quote{font-size:8.6px;margin-top:21px;color:var(--muted)}

  .connect{position:absolute;left:194px;top:525px}
  .connect h2{font-family:"Manrope",sans-serif;font-weight:800;font-size:19.5px;line-height:24px;color:var(--ink)}
  .connect p{font-size:9.6px;margin-top:10px}
  .social{display:flex;align-items:center;gap:5px;margin-top:9px;font-size:9px;color:var(--muted)}
  .social-dot{width:22px;height:22px;border-radius:50%;background:var(--white);border:1px solid var(--line)}

  .features{position:absolute;left:194px;top:644px;display:flex;gap:11px}
  .feature{width:263px;height:103px;background:var(--white);border:1px solid var(--line);border-radius:9px;padding:21px 10px}
  .feature h3{font-size:11.8px;font-weight:600;color:var(--card-title)}
  .feature p{font-size:9.6px;line-height:12px;margin-top:10px;color:var(--ink)}

  .site-footer{position:absolute;left:0;top:799px;width:1200px;height:91px;background:var(--white);border-top:1px solid var(--line)}
  .footer-inner{position:absolute;left:206px;top:13px}
  .tagline{font-size:10px;font-weight:600;color:var(--body)}
  .footer-links{font-size:9px;margin-top:3px;color:var(--muted)}
  .copyright{font-size:9px;margin-top:2px;color:var(--muted)}
  .footer-social{position:absolute;right:206px;top:12px;font-size:9px;color:var(--muted)}
  .footer-social .row{display:flex;gap:6px;margin-bottom:4px}
  .footer-social b{color:var(--body)}
</style>
</head>
<body>
  <header class="site-header">
    <div class="brand"><span class="brand-dot"></span><span class="brand-name">Meadow Lanterns</span></div>
    <nav class="main-nav">
      <a class="current" href="#">Home</a>
      <a href="#">How It Works</a>
      <a href="#">Ebook Store</a>
      <a href="#">Certification</a>
      <a href="#">Membership</a>
      <a href="#">About Me</a>
      <a href="#">Disclosure</a>
      <a class="btn-shop" href="#">Shop Ebooks</a>
    </nav>
  </header>

  <section class="hero-card">
    <span class="eyebrow">Calm starts here</span>
    <h1 class="hero-title">Meadow Lanterns: gentle tools and real support for your nervous system</h1>
    <p class="hero-lead">Daily encouragement, practical skills, and a community of courage. Learn to walk with fear and choose brave, compassionate steps forward—together.</p>
    <div class="hero-actions">
      <a class="btn btn-primary" href="#">How It Works</a>
      <a class="btn" href="#">Browse Ebooks</a>
      <a class="btn" href="#">Join Membership</a>
    </div>
  </section>

  <figure class="portrait-card">
    <div class="portrait" role="img" aria-label="Portrait photo of the site founder in a red patterned top and red glasses"></div>
    <figcaption class="portrait-quote">“I love hearing from others walking this path.” — The Meadow Lantern</figcaption>
  </figure>

  <section class="connect">
    <h2>Stay Connected</h2>
    <p>Follow Meadow Lantern for daily encouragement, calming tools, and community stories.</p>
    <div class="social">
      <span class="social-dot"></span><span class="social-dot"></span><span class="social-dot"></span>
      <span class="handle">@MeadowLanternHome</span>
    </div>
  </section>

  <section class="features">
    <article class="feature"><h3>Gentle Framework</h3><p>Simple steps to calm the body, shift thoughts, and build confidence. Start with the free overview on <a href="#">How it Works</a>.</p></article>
    <article class="feature"><h3>Ebooks &amp; Guides</h3><p>Concise, friendly resources with practical exercises. Visit the <a href="#">Ebook Store</a> for instant downloads.</p></article>
    <article class="feature"><h3>Grow Together</h3><p>Membership options for deeper support—Q&amp;A, live sessions, and community check-ins. Explore <a href="#">Membership</a>.</p></article>
  </section>

  <footer class="site-footer">
    <div class="footer-inner">
      <p class="tagline">🌿 Walking with fear, choosing courage, calming the nervous system together.</p>
      <p class="footer-links"><a href="#">Home</a> | <a href="#">About Me</a> | <a href="#">How It Works</a> | <a href="#">Ebook Store</a> | <a href="#">Certification</a> | <a href="#">Membership</a> | <a href="#">Disclosure</a></p>
      <p class="copyright">© 2025 MeadowLantern.com · All rights reserved</p>
    </div>
    <div class="footer-social">
      <div class="row"><span class="social-dot"></span><span class="social-dot"></span><span class="social-dot"></span></div>
      Follow <b>@MeadowLanternHome</b>
    </div>
  </footer>
</body>
</html>
```